Luxury Candle Startup Needs Modern Packaging Box & Matching Label Design

We are Wickhollow, a luxury candle company about to launch in Australia and we need a box packaging design that is modern, minimalist, and feminine. Our target audience are females, mostly mothers, within the age range of 25-45 who are looking for high quality, handmade luxurious products. Our company is going to have a large social media presence with new mothers as we are going to show our journey with starting a business whilst on maternity leave. We would like the arch shape incorporated into the box packaging as it is beautiful and symbolises moving into a new phase in life which really represents the brand. We would like for the packaging box to be a simple white box with a sleeve insert over the box with the design to make printing easier. Our colour inspiration are very earthy colours and would like the sleeve colour to be easily changed according to the scent. For example dusky rose coloured sleeve for rose patchouli and amber scent, light coffee coloured sleeve for coffee bean cacao scent etc. Please see uploaded files for inspiration, our logo, and the type of candle jars used.
The box dimensions are:
External Dimension: 95mmW x 95mmL x 116mmH
We look forward to seeing your amazing designs!

```html
<!DOCTYPE html>
<html lang="en">
<head>
<meta charset="utf-8">
<title>Wickhollow – Rose Patchouli Packaging</title>
<link rel="stylesheet" href="https://fonts.googleapis.com/css2?family=Raleway:wght@300;400;600&display=swap">
<style>
  :root {
    --canvas-grey: #f2f2f2;
    --sleeve-rose: #f6c3c6;
    --band-rose: #f9cdcf;
    --illustration-rose: #efb3b8;
    --ink-plum: #6e4a50;
    --ink-muted: #7d5a60;
  }
  * { margin: 0; padding: 0; box-sizing: border-box; }
  html, body { width: 1200px; height: 1200px; overflow: hidden; }
  body {
    background: var(--canvas-grey);
    font-family: "Raleway", sans-serif;
    color: var(--ink-plum);
    position: relative;
  }

  /* Box front panel, shown flat */
  .sleeve-front {
    position: absolute;
    left: 390px; top: 110px;
    width: 420px; height: 500px;
    background: var(--sleeve-rose);
  }
  .sleeve-front .rose-illustration {
    position: absolute;
    left: 30px; top: 40px;
    width: 220px; height: 300px;
    border-radius: 110px 110px 20px 20px;
    background: radial-gradient(circle at 55% 35%, var(--illustration-rose), rgba(239,179,184,0) 70%);
    opacity: .8;
  }
  .sleeve-front .label-block {
    position: absolute;
    left: 0; right: 0; top: 280px;
    text-align: center;
  }

  /* Label band */
  .label-band {
    position: absolute;
    left: 0; top: 870px;
    width: 1200px; height: 330px;
    background: var(--band-rose);
  }
  .label-band .rose-illustration {
    position: absolute;
    left: 300px; top: 14px;
    width: 230px; height: 300px;
    border-radius: 115px 115px 20px 20px;
    background: radial-gradient(circle at 45% 30%, var(--illustration-rose), rgba(239,179,184,0) 70%);
    opacity: .85;
  }
  .label-band .label-block {
    position: absolute;
    left: 463px; width: 400px; top: 72px;
    text-align: center;
  }

  .brand-name {
    font-weight: 400;
    font-size: 50px;
    letter-spacing: 4px;
    line-height: 1;
    color: var(--ink-plum);
    text-transform: uppercase;
  }
  .tagline {
    margin-top: 18px;
    font-weight: 600;
    font-size: 11px;
    letter-spacing: 2.5px;
    color: var(--ink-plum);
  }
  .origin {
    margin-top: 6px;
    font-weight: 600;
    font-size: 8px;
    letter-spacing: 2px;
    color: var(--ink-plum);
  }
  .scent-name {
    margin-top: 18px;
    font-weight: 400;
    font-size: 20px;
    letter-spacing: 1px;
    color: var(--ink-muted);
  }
  .sleeve-front .brand-name { font-size: 46px; }
  .sleeve-front .scent-name { font-size: 18px; }
</style>
</head>
<body>
  <section class="sleeve-front">
    <div class="rose-illustration" role="img" aria-label="Fine line drawing of a rose with stem and leaves"></div>
    <div class="label-block">
      <div class="brand-name">Wickhollow</div>
      <div class="tagline">LUXURY FRAGRANCE</div>
      <div class="origin">AUSTRALIA</div>
      <div class="scent-name">ROSE PATCHOULI</div>
    </div>
  </section>

  <section class="label-band">
    <div class="rose-illustration" role="img" aria-label="Fine line drawing of a rose with stem and leaves"></div>
    <div class="label-block">
      <div class="brand-name">Wickhollow</div>
      <div class="tagline">LUXURY FRAGRANCE</div>
      <div class="origin">AUSTRALIA</div>
      <div class="scent-name">ROSE PATCHOULI</div>
    </div>
  </section>
</body>
</html>
```